Email Signatures

I would like to create a new email signature for my team. The design will be the same for everyone, with only individual details such as name and email changing. You can also see our brand style on our website. https://www.tlmbespokehomes.com.au/

Target Market(s)

Clients for new builds or renovations

Industry/Entity Type

Construction

Colors

Designer to choose colors to be used in the design.

```html
<!DOCTYPE html>
<html lang="en">
<head>
<meta charset="utf-8">
<title>TLM Bespoke Homes – Email Signature</title>
<link href="https://fonts.googleapis.com/css2?family=Poppins:wght@400;700&display=swap" rel="stylesheet">
<style>
  :root {
    --page-bg: #e8e8e8;
    --card-bg: #1e1f21;
    --brand-green: #1a9645;
    --text-light: #ffffff;
    --watermark: #262729;
  }
  * { margin: 0; padding: 0; box-sizing: border-box; }
  html, body {
    width: 1200px; height: 526px; overflow: hidden;
    background: var(--page-bg);
    font-family: "Poppins", sans-serif;
  }
  .signature {
    position: absolute; left: 98px; top: 136px;
    width: 1004px; height: 254px;
    background: var(--card-bg);
    overflow: hidden;
  }
  .brand-watermark {
    position: absolute; left: 575px; top: 58px;
    font-weight: 700; font-size: 190px; line-height: 1;
    color: var(--watermark); letter-spacing: 6px;
  }
  .social-rail {
    position: absolute; left: 0; top: 35px;
    width: 43px; height: 185px;
    background: var(--brand-green);
  }
  .social-handle {
    position: absolute; left: 22px; top: 42px;
    transform: translate(-50%, -50%) rotate(-90deg);
    font-size: 10px; line-height: 1; color: var(--text-light); white-space: nowrap;
  }
  .social-links { position: absolute; left: 0; top: 0; }
  .brand-name {
    position: absolute; left: 76px; top: 110px;
    display: flex; align-items: center; gap: 10px;
  }
  .brand-mark {
    width: 14px; height: 14px; background: var(--brand-green); flex: none;
  }
  .brand-text {
    font-weight: 700; font-size: 19px; line-height: 1.15;
    color: var(--text-light); letter-spacing: 0.5px; white-space: nowrap;
  }
  .person {
    position: absolute; left: 293px; top: 53px;
  }
  .person-name {
    font-weight: 700; font-size: 26px; line-height: 1.1;
    color: var(--brand-green); white-space: nowrap;
  }
  .person-title {
    font-weight: 400; font-size: 16.5px; line-height: 1.3;
    color: var(--text-light);
  }
  .contact-list { position: absolute; left: 293px; top: 124.5px; list-style: none; }
  .contact-item {
    display: flex; align-items: center; gap: 7px;
    height: 19px; margin-bottom: 9.5px;
    font-size: 14.5px; color: var(--text-light); white-space: nowrap;
  }
  .contact-icon { width: 19px; height: 19px; flex: none; }
</style>
</head>
<body>
  <div class="signature">
    <div class="brand-watermark" aria-hidden="true">TLM</div>

    <aside class="social-rail">
      <span class="social-handle">@username</span>
      <svg class="social-links" width="43" height="185" viewBox="0 0 43 185" aria-label="Social profiles">
        <circle cx="22" cy="92" r="8" fill="#fff"/>
        <circle cx="22" cy="116" r="8" fill="#fff"/>
        <circle cx="22" cy="140" r="8" fill="#fff"/>
        <circle cx="22" cy="163" r="8" fill="#fff"/>
      </svg>
    </aside>

    <div class="brand-name">
      <span class="brand-mark"></span>
      <span class="brand-text">TLM<br>BESPOKE HOMES</span>
    </div>

    <div class="person">
      <p class="person-name">DANIEL J. HARLOW</p>
      <p class="person-title">Managing Director</p>
    </div>

    <ul class="contact-list">
      <li class="contact-item">
        <svg class="contact-icon" viewBox="0 0 19 19"><rect width="19" height="19" rx="2" fill="#1a9645"/><path d="M6 4.5l2 2.3-1 1.4c.7 1.4 1.8 2.5 3.2 3.2l1.4-1 2.3 2-1.2 1.8C9 14 5 10 4.5 5.7z" fill="#1e1f21"/></svg>
        <span>+00 123 456 78</span>
      </li>
      <li class="contact-item">
        <svg class="contact-icon" viewBox="0 0 19 19"><rect width="19" height="19" rx="2" fill="#1a9645"/><rect x="3.5" y="5.5" width="12" height="8" fill="none" stroke="#1e1f21" stroke-width="1.3"/><path d="M3.5 5.5l6 4.5 6-4.5M3.5 13.5l4.5-4M15.5 13.5l-4.5-4" fill="none" stroke="#1e1f21" stroke-width="1.2"/></svg>
        <span>company@email.com</span>
      </li>
      <li class="contact-item">
        <svg class="contact-icon" viewBox="0 0 19 19"><rect width="19" height="19" rx="2" fill="#1a9645"/><path d="M6.5 3.5v11l2.6-2.5 2 4 1.5-.7-2-4h3.6z" fill="#1e1f21"/></svg>
        <span>www.companywebsite.com</span>
      </li>
    </ul>
  </div>
</body>
</html>
```